Kestrel Ridge Holdings pty ltd - Facebook

Professional landing page.

Highlights our dedication to Australian Farmers and to our cause.

Play around with it as much as you want. A blended photo showing all industries on 1/3 if possible. Go nuts.

It Professional

```html
<!DOCTYPE html>
<html lang="en">
<head>
<meta charset="utf-8">
<title>Kestrel Ridge Holdings – Page Cover</title>
<link rel="stylesheet" href="https://fonts.googleapis.com/css2?family=Saira:wght@600&display=swap">
<style>
  :root {
    --canvas: #ffffff;
    --sky-top: #f4d36a;
    --sky-glow: #f1c23f;
    --horizon: #b49a45;
    --hills: #4a5f33;
    --treeline: #2f4a1e;
    --field-light: #4f9a22;
    --field-mid: #3b7e18;
    --field-dark: #1e4a0d;
    --brand-ink: #e3ea7a;
    --brand-mark: #c9d94a;
    --frame: #ffffff;
  }
  * { box-sizing: border-box; margin: 0; padding: 0; }
  html, body {
    width: 1200px;
    height: 1000px;
    overflow: hidden;
    background: var(--canvas);
  }
  .page-art { position: relative; width: 1200px; height: 1000px; }

  .cover {
    position: absolute;
    left: 37px;
    top: 211px;
    width: 1129px;
    height: 427px;
    overflow: hidden;
  }
  .cover-photo {
    position: absolute;
    inset: 0;
    background:
      radial-gradient(ellipse 45% 30% at 62% 18%, rgba(255,236,150,0.85) 0%, rgba(255,236,150,0) 100%),
      linear-gradient(180deg,
        var(--sky-top) 0%,
        var(--sky-glow) 18%,
        var(--horizon) 28%,
        var(--hills) 33%,
        var(--treeline) 38%,
        var(--field-light) 45%,
        var(--field-mid) 70%,
        var(--field-dark) 100%);
  }
  .brand-square { display: block; background: var(--brand-mark); }
  .cover-square {
    position: absolute;
    left: 290px;
    top: 150px;
    width: 110px;
    height: 110px;
  }
  .cover-wordmark {
    position: absolute;
    right: 76px;
    top: 200px;
    text-align: right;
    font-family: "Saira", sans-serif;
    font-weight: 600;
    color: var(--brand-ink);
  }
  .wordmark-main {
    display: block;
    font-size: 80px;
    line-height: 0.95;
    letter-spacing: 1px;
  }
  .wordmark-sub {
    display: block;
    font-size: 40px;
    line-height: 1.05;
    letter-spacing: 6px;
    text-transform: uppercase;
    margin-right: -6px;
  }

  .profile-tile {
    position: absolute;
    left: 59px;
    top: 443px;
    width: 231px;
    height: 234px;
    border: 5px solid var(--frame);
    box-shadow: 0 2px 4px rgba(0,0,0,0.35);
    overflow: hidden;
  }
  .profile-photo {
    position: absolute;
    inset: 0;
    background: radial-gradient(circle at 50% 45%, var(--field-light) 0%, var(--field-mid) 55%, var(--field-dark) 100%);
  }
  .profile-brand {
    position: absolute;
    left: 12px;
    top: 86px;
    display: flex;
    align-items: center;
    gap: 10px;
  }
  .profile-brand .brand-square { width: 52px; height: 52px; }
  .profile-name {
    font-family: "Saira", sans-serif;
    font-weight: 600;
    font-size: 68px;
    line-height: 1;
    color: var(--brand-ink);
  }
</style>
</head>
<body>
  <main class="page-art">
    <section class="cover">
      <div class="cover-photo" role="img" aria-label="Painterly photograph of green Australian farm pasture under a golden sunrise sky with distant hills and a treeline"></div>
      <span class="brand-square cover-square"></span>
      <h1 class="cover-wordmark">
        <span class="wordmark-main">Kestrel Ridge</span>
        <span class="wordmark-sub">Holdings</span>
      </h1>
    </section>
    <section class="profile-tile">
      <div class="profile-photo" role="img" aria-label="Close painterly texture of green pasture grass"></div>
      <div class="profile-brand">
        <span class="brand-square"></span>
        <span class="profile-name">KRH</span>
      </div>
    </section>
  </main>
</body>
</html>
```